UI/ UX Design for ERP Software

We need a new UX/UI interface for a ERP software for property managers. Our CMMS / ERP solution is made based on responsive design technologies and is coded in PHP.
The overall UX to be similar to Zel Kavo - easy navigation, intuitive menus.

Industry/Entity Type

Property Management

Number of Pages Required

5+ page

Requirements
Must have
• Round dock buttons
Consistent icons across the application
Enough Spacing between buttons/icons/ menu
Consistent Font
Nice to have
• We would like the UX to allow the users to use the application without /minimum training.
Should not have
• we don't want anything that is classic with respect to UX

```html
<!DOCTYPE html>
<html lang="en">
<head>
<meta charset="utf-8">
<title>Meridian Tower – General Info</title>
<link href="https://fonts.googleapis.com/css2?family=Poppins:wght@400;500;600;700&display=swap" rel="stylesheet">
<style>
:root{
  --bg:#eef0f4;
  --white:#ffffff;
  --sidebar:#56667f;
  --sidebar-line:#66758c;
  --accent:#1e90ff;
  --accent-2:#2aa8ff;
  --green:#9ccf6a;
  --ink:#4a5566;
  --ink-soft:#5e6775;
  --row:#f4f4f5;
  --field:#efeff1;
  --dot:#1e90ff;
}
*{box-sizing:border-box;margin:0;padding:0}
html,body{width:1200px;height:800px;overflow:hidden}
body{font-family:"Poppins",sans-serif;background:var(--bg);position:relative;color:var(--ink)}
.topbar{position:absolute;left:0;top:0;width:1200px;height:89px;background:var(--white);box-shadow:0 2px 8px rgba(0,0,0,.05);z-index:2}
.brand{position:absolute;left:36px;top:28px;display:flex;align-items:center;gap:8px}
.brand-mark{width:26px;height:26px;border-radius:50%;background:var(--accent)}
.brand-name{font-size:26px;font-weight:600;color:var(--accent)}
.search{position:absolute;left:277px;top:27px;width:230px;height:35px;border-radius:18px;background:var(--field);display:flex;align-items:center;padding:0 16px;font-size:13px;color:#8a8f98;justify-content:space-between}
.sort{position:absolute;left:516px;top:27px;width:95px;height:35px;border-radius:18px;background:var(--field);display:flex;align-items:center;justify-content:space-between;padding:0 16px;font-size:12px;color:#8a8f98}
.tool{position:absolute;top:24px;width:43px;height:42px;border-radius:8px;background:var(--field);display:flex;align-items:center;justify-content:center}
.divider{position:absolute;left:1030px;top:27px;width:1px;height:36px;background:#e4e6ea}
.avatar{position:absolute;top:24px;width:42px;height:42px;border-radius:50%;border:2px solid var(--white)}
.add-btn{position:absolute;left:1120px;top:24px;width:43px;height:43px;border-radius:50%;background:#4f5c70;color:#fff;font-size:24px;display:flex;align-items:center;justify-content:center;font-weight:400}
.sidebar{position:absolute;left:0;top:89px;width:251px;height:711px;background:var(--sidebar)}
.nav-item{position:absolute;left:30px;width:183px;height:53px;display:flex;align-items:center;gap:10px;color:#fff;font-size:13.5px;font-weight:500;border-bottom:1px solid var(--sidebar-line);white-space:nowrap}
.nav-item svg{flex:none}
.nav-item.is-active{left:19px;width:201px;height:43px;border-radius:22px;background:linear-gradient(90deg,var(--accent-2),var(--accent));border:none;padding-left:14px;font-size:16px;font-weight:600}
.nav-item.no-line{border-bottom:none}
.page-title{position:absolute;left:284px;top:126px;font-size:28px;font-weight:600;color:var(--ink)}
.crumbs{position:absolute;right:36px;top:138px;display:flex;align-items:center;gap:7px;font-size:13px;font-weight:500;color:var(--ink)}
.card{position:absolute;left:284px;top:186px;width:880px;height:640px;background:var(--white);border-radius:6px;box-shadow:0 2px 10px rgba(0,0,0,.04)}
.card-heading{position:absolute;font-size:18.5px;font-weight:600;color:var(--ink)}
.edit-btn{position:absolute;left:247px;top:22px;height:37px;padding:0 16px;border-radius:19px;background:var(--green);color:#fff;font-size:13px;font-weight:600;display:flex;align-items:center;gap:6px}
.info-list{position:absolute;left:35px;top:80px;width:459px;list-style:none}
.info-list li{height:35.5px;display:flex;align-items:center;font-size:12.5px;padding-left:22px;border-radius:3px;white-space:nowrap}
.info-list li:nth-child(even){background:var(--row)}
.info-list .label{width:190px;flex:none;font-weight:500;color:var(--ink);display:flex;align-items:center;gap:14px}
.info-list .label::before{content:"";width:7px;height:7px;border-radius:50%;border:2px solid var(--dot)}
.info-list .value{color:var(--ink-soft)}
.scroll-thumb{position:absolute;width:4px;border-radius:2px;background:#dcdde0}
.photo{position:absolute;left:557px;width:287px;height:213px;border-radius:4px}
</style>
</head>
<body>
<header class="topbar">
  <div class="brand"><span class="brand-mark"></span><span class="brand-name">Keystead</span></div>
  <div class="search">Search...
    <svg width="18" height="18" viewBox="0 0 24 24" fill="none" stroke="#333" stroke-width="2.2"><circle cx="10" cy="10" r="7"/><path d="M15 15l6 6"/></svg>
  </div>
  <div class="sort">A-Z
    <svg width="10" height="10" viewBox="0 0 10 10" fill="none" stroke="#333" stroke-width="1.6"><path d="M2 4l3 3 3-3"/></svg>
  </div>
  <div class="tool" style="left:837px">
    <svg width="22" height="22" viewBox="0 0 24 24" fill="none" stroke="#4f5c70" stroke-width="1.8"><path d="M6 17V11a6 6 0 0112 0v6l2 2H4z"/><path d="M10 21h4"/><circle cx="17" cy="6" r="3" fill="#f04b4b" stroke="none"/></svg>
  </div>
  <div class="tool" style="left:900px">
    <svg width="22" height="22" viewBox="0 0 24 24" fill="none" stroke="#4f5c70" stroke-width="1.8"><path d="M3 4h18v13H9l-5 4z"/><path d="M7 9h10M7 13h7"/></svg>
  </div>
  <div class="tool" style="left:962px">
    <svg width="22" height="22" viewBox="0 0 24 24" fill="none" stroke="#4f5c70" stroke-width="1.8"><path d="M3 6h7l2 2h9v12H3z"/><circle cx="14" cy="14" r="3"/><path d="M16 16l3 3"/></svg>
  </div>
  <div class="divider"></div>
  <div class="avatar" role="img" aria-label="Team member avatar" style="left:1056px;background:linear-gradient(#c98a5a,#3a3a3a)"></div>
  <div class="avatar" role="img" aria-label="Team member avatar" style="left:1087px;background:linear-gradient(#c9b8f0,#e7c8a8)"></div>
  <div class="add-btn">+</div>
</header>

<nav class="sidebar">
  <div class="nav-item is-active" style="top:39px">
    <svg width="20" height="20" viewBox="0 0 24 24" fill="none" stroke="#fff" stroke-width="2"><circle cx="12" cy="13" r="9"/><path d="M12 13l4-4"/></svg>General Info</div>
  <div class="nav-item" style="top:87px"><svg width="22" height="22" viewBox="0 0 24 24" fill="none" stroke="#fff" stroke-width="1.6"><circle cx="9" cy="8" r="4"/><path d="M2 21a7 7 0 0114 0M16 4a4 4 0 010 8M18 14a6 6 0 014 7"/></svg>Organization Chart</div>
  <div class="nav-item" style="top:147px"><svg width="22" height="22" viewBox="0 0 24 24" fill="none" stroke="#fff" stroke-width="1.6"><path d="M3 11l9-8 9 8M5 9v12h14V9"/></svg>Tenant List</div>
  <div class="nav-item" style="top:207px"><svg width="22" height="22" viewBox="0 0 24 24" fill="none" stroke="#fff" stroke-width="1.6"><path d="M3 11l9-8 9 8M5 9v12h14V9"/><rect x="9" y="12" width="6" height="5"/></svg>Property Assets</div>
  <div class="nav-item" style="top:267px"><svg width="22" height="22" viewBox="0 0 24 24" fill="none" stroke="#fff" stroke-width="1.6"><rect x="5" y="3" width="15" height="18" rx="1"/><circle cx="12.5" cy="10" r="3"/><path d="M8 17a4.5 4.5 0 019 0M3 7h3M3 12h3M3 17h3"/></svg>Contractors List</div>
  <div class="nav-item" style="top:327px"><svg width="22" height="22" viewBox="0 0 24 24" fill="none" stroke="#fff" stroke-width="1.6"><circle cx="12" cy="7" r="4"/><path d="M7 7h10M4 21v-3a5 5 0 015-5h6a5 5 0 015 5v3z"/></svg>Compliance Manag...</div>
  <div class="nav-item" style="top:387px"><svg width="22" height="22" viewBox="0 0 24 24" fill="none" stroke="#fff" stroke-width="1.6"><circle cx="9" cy="8" r="4"/><path d="M2 21a7 7 0 0114 0M16 4a4 4 0 010 8M18 14a6 6 0 014 7"/></svg>Maint. Work Orders</div>
  <div class="nav-item" style="top:447px"><svg width="22" height="22" viewBox="0 0 24 24" fill="none" stroke="#fff" stroke-width="1.6"><rect x="2" y="5" width="20" height="14" rx="3"/><circle cx="8" cy="12" r="3"/><path d="M14 10h5M14 14h5"/></svg>Work Orders</div>
  <div class="nav-item" style="top:507px"><svg width="22" height="22" viewBox="0 0 24 24" fill="none" stroke="#fff" stroke-width="1.6"><path d="M2 4h3l3 12h12l2-8H7"/><circle cx="9" cy="20" r="1.5"/><circle cx="18" cy="20" r="1.5"/><circle cx="14" cy="6" r="3"/></svg>Purchase Orders</div>
  <div class="nav-item no-line" style="top:567px"><svg width="22" height="22" viewBox="0 0 24 24" fill="none" stroke="#fff" stroke-width="1.6"><rect x="4" y="3" width="16" height="18" rx="1"/><path d="M8 8h8M8 12h8M8 16h4"/></svg>Files</div>
</nav>

<main>
  <h1 class="page-title">Meridian Tower</h1>
  <div class="crumbs">
    <svg width="15" height="14" viewBox="0 0 24 22" fill="#4a5566"><path d="M12 1L1 11h3v10h6v-6h4v6h6V11h3z"/></svg>
    HOME <span>/</span> PROPERTIES
  </div>

  <section class="card">
    <h2 class="card-heading" style="left:35px;top:30px">General Information</h2>
    <div class="edit-btn">
      <svg width="15" height="15" viewBox="0 0 24 24" fill="none" stroke="#fff" stroke-width="2.2"><path d="M11 4H4v16h16v-7"/><path d="M18 2l4 4-10 10H8v-4z"/></svg>PROPERTY EDIT</div>

    <ul class="info-list">
      <li><span class="label">PROVINCE:</span><span class="value">British Columbia</span></li>
      <li><span class="label">CITY:</span><span class="value">Acton Vale</span></li>
      <li><span class="label">ADDRESS:</span><span class="value">42 Harbourline Road, Vancouver, BC</span></li>
      <li><span class="label">GPS ADDRESS:</span><span class="value">48.7413205 : -121-40815300000004</span></li>
      <li><span class="label">POSTAL CODE:</span><span class="value">V6x 2K8</span></li>
      <li><span class="label">DATE BUILT:</span><span class="value">07/01/1980</span></li>
      <li><span class="label">AREA (SQ.FT):</span><span class="value">150000.00</span></li>
      <li><span class="label">LOT SIZE:</span><span class="value"></span></li>
      <li><span class="label">ZONING:</span><span class="value">CDI</span></li>
      <li><span class="label">STRUCTURE TYPE:</span><span class="value">Seel and concreate</span></li>
      <li><span class="label">BUILDING HEIGHT:</span><span class="value">250</span></li>
      <li><span class="label">CLEAR HEIGHT:</span><span class="value"></span></li>
      <li><span class="label">FLOOR LOADING CAPACITY:</span><span class="value">50</span></li>
      <li><span class="label">NUMBER OF FLOORS:</span><span class="value">30</span></li>
      <li><span class="label">SUITES</span><span class="value">150</span></li>
    </ul>
    <div class="scroll-thumb" style="left:507px;top:325px;height:50px"></div>

    <h2 class="card-heading" style="left:555px;top:30px">General Information</h2>
    <div class="photo" role="img" aria-label="Photo of the tower's angular glass facade" style="top:79px;background:linear-gradient(160deg,#e6ecf1 0%,#c7d0d8 60%,#8f9aa5 100%)"></div>
    <div class="photo" role="img" aria-label="Photo of the tower's tiled upper volume from below" style="top:301px;background:linear-gradient(170deg,#dfe2e6 0%,#cfd4da 55%,#a9b1ba 100%)"></div>
    <div class="photo" role="img" aria-label="Photo of white balconies against a pale sky" style="top:523px;background:linear-gradient(180deg,#c9dbe7 0%,#eef2f5 100%)"></div>
    <div class="scroll-thumb" style="left:855px;top:348px;height:130px"></div>
  </section>
</main>
</body>
</html>
```